Consulting firm needs an infographic

The consulting we do needs a very graphic and understandable way to have perspective clients get exactly where we can help their company grow. I designed something that needs a lot of spice for it to look professional and relatable to them. This is being created to be used on a business card, as well as on posters, and social media.

```html
<!DOCTYPE html>
<html lang="en">
<head>
<meta charset="utf-8">
<title>Growth Framework Infographic</title>
<link rel="stylesheet" href="https://fonts.googleapis.com/css2?family=Roboto:ital,wght@0,500;0,700;1,300&family=Roboto+Condensed:wght@700&display=swap">
<style>
  :root {
    --bg: #ffffff;
    --teal-dark: #10716d;
    --teal-mid: #5ba8ab;
    --teal-pale: #accfd1;
    --teal: #1e9a9a;
    --yellow: #f5e614;
    --red: #ee3932;
    --red-soft: #f38b73;
    --red-mid: #ef6a51;
    --orange: #f4a81e;
    --orange-soft: #f9c77c;
    --orange-mid: #f5b850;
    --green: #a6d04a;
    --green-soft: #cae190;
    --green-mid: #b7d971;
    --arrow: #d3d3d7;
    --ink: #1d1d1b;
    --white: #ffffff;
  }
  html, body {
    margin: 0;
    width: 1200px;
    height: 960px;
    overflow: hidden;
    background: var(--bg);
  }
  .infographic { display: block; width: 1200px; height: 960px; }
  .title { font-family: "Roboto Condensed", "Roboto", sans-serif; font-weight: 700; font-size: 58px; fill: var(--yellow); }
  .subtitle { font-family: "Roboto", sans-serif; font-weight: 300; font-style: italic; font-size: 36px; fill: var(--yellow); }
  .label { font-family: "Roboto", sans-serif; font-weight: 500; font-size: 30px; fill: var(--white); }
  .divider { stroke: var(--white); stroke-width: 6; fill: none; }
  .flow-line { stroke: var(--arrow); stroke-width: 9; fill: none; }
  .flow-head { fill: var(--arrow); }
  .icon { stroke: var(--white); stroke-width: 3.5; fill: none; stroke-linecap: round; stroke-linejoin: round; }
  .icon-fill { fill: var(--white); }
  .brand-name { font-family: "Roboto", sans-serif; font-weight: 700; font-size: 46px; fill: var(--ink); }
  .brand-dot { fill: var(--ink); }
</style>
</head>
<body>
<svg class="infographic" viewBox="0 0 2151 1720" xmlns="http://www.w3.org/2000/svg" role="img" aria-label="Business growth framework: company, vendors, executive and customers">

  <!-- Company triangle -->
  <g class="company">
    <polygon points="724,202 1431,202 1338,388 817,388" fill="var(--teal-dark)"/>
    <polygon points="817,388 1078,388 1078,545 933,622" fill="var(--teal-mid)"/>
    <polygon points="1078,388 1338,388 1223,622 1078,545" fill="var(--teal-pale)"/>
    <polygon points="933,622 1078,545 1223,622 1078,910" fill="var(--teal)"/>
    <line class="divider" x1="810" y1="391" x2="1345" y2="391"/>
    <polyline class="divider" points="1078,391 1078,545"/>
    <polyline class="divider" points="930,624 1078,545 1226,624"/>
    <text class="title" x="1078" y="287" text-anchor="middle">YOUR COMPANY</text>
    <text class="subtitle" x="1078" y="340" text-anchor="middle">Products/Services</text>
    <text class="label" x="965" y="450" text-anchor="middle">Workforce</text>
    <text class="label" x="1191" y="450" text-anchor="middle">Workplace</text>
    <text class="label" x="1078" y="648" text-anchor="middle">Workflow</text>

    <g class="icon-workforce">
      <circle class="icon-fill" cx="946" cy="484" r="8"/>
      <circle class="icon-fill" cx="973" cy="488" r="8"/>
      <circle class="icon-fill" cx="1000" cy="484" r="8"/>
      <path class="icon-fill" d="M933 508 q13-18 26 0z M960 512 q13-18 26 0z M987 508 q13-18 26 0z"/>
      <circle class="icon" cx="973" cy="516" r="26"/>
    </g>
    <g class="icon-workplace">
      <rect class="icon" x="1146" y="492" width="30" height="22" rx="3"/>
      <line class="icon" x1="1146" y1="520" x2="1176" y2="520"/>
      <line class="icon" x1="1150" y1="520" x2="1150" y2="545"/>
      <line class="icon" x1="1172" y1="520" x2="1172" y2="545"/>
      <rect class="icon" x="1184" y="480" width="28" height="20"/>
      <rect class="icon" x="1182" y="505" width="36" height="40"/>
      <line class="icon" x1="1182" y1="525" x2="1218" y2="525"/>
    </g>
    <g class="icon-workflow">
      <circle class="icon-fill" cx="1078" cy="691" r="11"/>
      <polyline class="icon" points="1078,702 1078,712 1038,712 1038,726"/>
      <polyline class="icon" points="1078,712 1118,712 1118,726"/>
      <line class="icon" x1="1078" y1="712" x2="1078" y2="726"/>
      <rect class="icon" x="1028" y="726" width="20" height="20"/>
      <rect class="icon" x="1068" y="726" width="20" height="20"/>
      <rect class="icon" x="1108" y="726" width="20" height="20"/>
    </g>
  </g>

  <!-- Vendors triangle -->
  <g class="vendors">
    <polygon points="583,700 727,988 583,1067 439,988" fill="var(--red)"/>
    <polygon points="439,988 583,1067 583,1220 323,1220" fill="var(--red-soft)"/>
    <polygon points="583,1067 727,988 842,1220 583,1220" fill="var(--red-mid)"/>
    <polyline class="divider" points="437,987 583,1067 729,987"/>
    <line class="divider" x1="583" y1="1067" x2="583" y2="1222"/>
    <text class="label" x="583" y="987" text-anchor="middle">Vendors</text>
    <text class="label" x="469" y="1176" text-anchor="middle">Resources</text>
    <text class="label" x="696" y="1176" text-anchor="middle">Costs</text>

    <g class="icon-handshake">
      <path class="icon" d="M540 890 l22-12 l30 22 l-28 32 z"/>
      <path class="icon" d="M626 888 l-22-12 l-34 14 l18 16 l14-8 l16 20 z"/>
      <path class="icon" d="M560 918 l8 8 M570 910 l10 10 M580 902 l10 10"/>
    </g>
    <g class="icon-resources">
      <circle class="icon" cx="473" cy="1082" r="14"/>
      <circle class="icon" cx="473" cy="1082" r="5"/>
      <path class="icon" d="M444 1115 h22 q10 0 10 8 h-16 M444 1132 h36 l26-22"/>
    </g>
    <g class="icon-costs">
      <path class="icon-fill" d="M688 1066 h24 l-6 12 q28 20 22 46 q-4 10 -28 10 q-24 0 -28-10 q-6-26 22-46z"/>
      <text x="700" y="1121" text-anchor="middle" font-family="Roboto, sans-serif" font-weight="700" font-size="28" fill="var(--red-mid)">$</text>
    </g>
  </g>

  <!-- Customers triangle -->
  <g class="customers">
    <polygon points="1573,700 1717,988 1573,1067 1429,988" fill="var(--orange)"/>
    <polygon points="1429,988 1573,1067 1573,1220 1313,1220" fill="var(--orange-soft)"/>
    <polygon points="1573,1067 1717,988 1832,1220 1573,1220" fill="var(--orange-mid)"/>
    <polyline class="divider" points="1427,987 1573,1067 1719,987"/>
    <line class="divider" x1="1573" y1="1067" x2="1573" y2="1222"/>
    <text class="label" x="1573" y="987" text-anchor="middle">Customers</text>
    <text class="label" x="1460" y="1176" text-anchor="middle">Identity &amp; B&amp;M</text>
    <text class="label" x="1687" y="1176" text-anchor="middle">Revenue</text>

    <g class="icon-customers">
      <circle class="icon" cx="1545" cy="883" r="8"/>
      <circle class="icon" cx="1573" cy="887" r="8"/>
      <circle class="icon" cx="1601" cy="883" r="8"/>
      <circle class="icon" cx="1555" cy="906" r="8"/>
      <circle class="icon" cx="1591" cy="906" r="8"/>
      <circle class="icon" cx="1573" cy="918" r="8"/>
      <path class="icon" d="M1530 910 q0-14 15-14 M1616 910 q0-14-15-14 M1538 935 q0-16 17-16 M1608 935 q0-16-17-16 M1556 944 q0-16 17-16 q17 0 17 16z"/>
    </g>
    <g class="icon-identity">
      <path class="icon" d="M1428 1100 l34-14 v40 l-34-14 z"/>
      <path class="icon" d="M1462 1086 l18-10 v58 l-18-8"/>
      <path class="icon" d="M1436 1114 l8 18 h8 l-4-16"/>
      <circle class="icon" cx="1495" cy="1086" r="14"/>
      <line class="icon" x1="1490" y1="1106" x2="1500" y2="1106"/>
    </g>
    <g class="icon-revenue">
      <rect class="icon-fill" x="1649" y="1112" width="10" height="20"/>
      <rect class="icon-fill" x="1665" y="1102" width="10" height="30"/>
      <rect class="icon-fill" x="1681" y="1092" width="10" height="40"/>
      <rect class="icon-fill" x="1697" y="1082" width="10" height="50"/>
      <path class="icon" d="M1648 1098 q34-6 56-30"/>
      <polygon class="icon-fill" points="1706,1062 1694,1066 1704,1076"/>
    </g>
  </g>

  <!-- Executive triangle -->
  <g class="executive">
    <polygon points="1078,1005 1222,1292 1078,1370 935,1292" fill="var(--green)"/>
    <polygon points="935,1292 1078,1370 1078,1523 819,1523" fill="var(--green-soft)"/>
    <polygon points="1078,1370 1222,1292 1337,1523 1078,1523" fill="var(--green-mid)"/>
    <polyline class="divider" points="933,1291 1078,1370 1224,1291"/>
    <line class="divider" x1="1078" y1="1370" x2="1078" y2="1525"/>
    <text class="label" x="1078" y="1252" text-anchor="middle">Executive</text>
    <text class="label" x="1078" y="1286" text-anchor="middle">(Administrative)</text>
    <text class="label" x="965" y="1478" text-anchor="middle">Personnel</text>
    <text class="label" x="1191" y="1478" text-anchor="middle">Logistics</text>

    <g class="icon-executive">
      <circle class="icon-fill" cx="1078" cy="1167" r="13"/>
      <path class="icon-fill" d="M1055 1208 q0-26 23-26 q23 0 23 26z"/>
    </g>
    <g class="icon-personnel">
      <circle class="icon-fill" cx="942" cy="1403" r="9"/>
      <circle class="icon-fill" cx="970" cy="1407" r="9"/>
      <circle class="icon-fill" cx="998" cy="1403" r="9"/>
      <path class="icon-fill" d="M927 1428 q15-20 30 0z M955 1432 q15-20 30 0z M983 1428 q15-20 30 0z"/>
    </g>
    <g class="icon-logistics">
      <polygon class="icon" points="1152,1408 1170,1402 1188,1410 1204,1404 1204,1436 1188,1442 1170,1434 1152,1440"/>
      <line class="icon" x1="1170" y1="1402" x2="1170" y2="1434"/>
      <line class="icon" x1="1188" y1="1410" x2="1188" y2="1442"/>
      <circle class="icon-fill" cx="1198" cy="1404" r="6"/>
    </g>
  </g>

  <!-- Cycle arrows -->
  <g class="flow">
    <path class="flow-line" d="M780 390 H640 Q586 390 586 445 V630"/>
    <polygon class="flow-head" points="565,628 607,628 586,665"/>
    <path class="flow-line" d="M1573 665 V445 Q1573 390 1518 390 H1416"/>
    <polygon class="flow-head" points="1418,368 1418,412 1380,390"/>
    <path class="flow-line" d="M586 1245 V1393 Q586 1447 640 1447 H762"/>
    <polygon class="flow-head" points="760,1426 760,1468 797,1447"/>
    <path class="flow-line" d="M1362 1447 H1518 Q1573 1447 1573 1392 V1282"/>
    <polygon class="flow-head" points="1552,1284 1594,1284 1573,1245"/>
  </g>

  <!-- Brand -->
  <g class="brand">
    <circle class="brand-dot" cx="1712" cy="331" r="12"/>
    <text class="brand-name" x="1736" y="347">Sproutwise</text>
  </g>
</svg>
</body>
</html>
```